VALMIKE GROUP

This is a company that provides executive protection. Our motto is "New Era in Protection"... I don't want this to look like other security websites. I want it to be clean and sharp and represent a new era. We are based in the bay area so maybe a picture of San Francisco in the background?
I want it to be able to funnel down a couple different categories.
1. About Us
2. Services (Executive Protection, Covert Protection, Residential Protection & Intelligence)
3. Iron Finch (Training & Consulting)
4. Contact Us
I want it to be very clean and modern. I don't want there to be any pictures of bodyguards with ear pieces like every other website.
Target Market(s)
Ultra High Net Worth Individuals
Coding
Coded - Design and coding required
Number of Pages Required
1 page
Requirements
Must have
- Colors of my Symbol
Nice to have
- City in the background, San Francisco, New York or the Pinehallow Club in Montana.
Should not have
- Should not look like an KVM website or have photos of bodyguards. I want this to be a clean and simple website with my logo

```html
<!DOCTYPE html>
<html lang="en">
<head>
<meta charset="utf-8">
<title>VALMIKE GROUP — New Era in Protection</title>
<link href="https://fonts.googleapis.com/css2?family=Raleway:wght@400;500;600;700&display=swap" rel="stylesheet">
<style>
  :root {
    --cream: #f2e4cf;
    --crimson: #6b1618;
    --slate: #2b3a48;
    --ink: #2d2d2d;
    --muted: #8a8078;
    --white: #ffffff;
  }
  * { margin: 0; padding: 0; box-sizing: border-box; }
  html, body {
    width: 1200px; height: 4145px; overflow: hidden;
    background: var(--cream);
    font-family: "Raleway", sans-serif;
    color: var(--slate);
  }
  .page { position: relative; width: 1200px; height: 4145px; }

  /* navigation */
  .site-nav { position: absolute; left: 0; top: 0; width: 1200px; height: 110px; background: var(--cream); }
  .nav-link { position: absolute; top: 40px; font-size: 24px; font-weight: 500; color: var(--ink); text-decoration: none; }
  .brand { position: absolute; left: 492px; top: 30px; width: 200px; text-align: center; }
  .brand-mark { display: block; width: 26px; height: 26px; margin: 0 auto 6px; background: var(--crimson); }
  .brand-name { font-size: 17px; font-weight: 700; letter-spacing: 1px; color: var(--crimson); }

  /* hero (children positioned relative to the hero, which starts at 110px) */
  .hero { position: absolute; left: 0; top: 110px; width: 1200px; height: 743px;
    background: linear-gradient(180deg, #7fb3d6 0%, #c9dde6 30%, #e8e1d2 48%, #8a6a52 62%, #6b4a35 78%, #4a3427 100%); }
  .hero-glow { position: absolute; right: 0; top: 360px; width: 420px; height: 300px;
    background: radial-gradient(ellipse at 90% 40%, rgba(255,190,110,.85), rgba(255,160,80,0) 70%); }
  .hero-title { position: absolute; top: 106px; left: 0; width: 1200px; text-align: center; font-size: 61px; line-height: 72px; font-weight: 700; color: var(--slate); letter-spacing: -0.5px; }
  .hero-sub { position: absolute; top: 182px; left: 0; width: 1160px; text-align: center; font-size: 24px; line-height: 30px; font-weight: 600; color: var(--crimson); }

  /* buttons */
  .btn-solid { position: absolute; display: flex; align-items: center; justify-content: center;
    background: var(--crimson); color: var(--white); font-size: 28px; font-weight: 600; text-decoration: none; }
  .btn-outline { position: absolute; display: flex; align-items: center; justify-content: center;
    border: 3px solid var(--crimson); color: var(--crimson); font-size: 29px; font-weight: 600; text-decoration: none; }

  /* section text */
  .eyebrow { position: absolute; font-size: 28px; font-weight: 700; color: var(--crimson); }
  .heading { position: absolute; font-size: 54px; font-weight: 700; color: var(--slate); line-height: 63px; white-space: nowrap; }
  .subhead { position: absolute; font-size: 29px; font-weight: 700; color: var(--slate); }
  .body-copy { position: absolute; font-size: 30px; font-weight: 400; line-height: 35px; color: var(--slate); }

  .photo { position: absolute; }

  /* service cards */
  .service-card { position: absolute; top: 1956px; width: 417px; height: 417px; border-radius: 6px; overflow: hidden; }
  .card-title { position: absolute; left: 21px; top: 335px; font-size: 25px; font-weight: 500; color: var(--ink); white-space: nowrap; }
  .card-link { position: absolute; left: 21px; top: 372px; font-size: 19px; font-weight: 500; color: var(--crimson); text-decoration: underline; white-space: nowrap; }

  /* contact form */
  .field { position: absolute; border: 3px solid var(--crimson); background: transparent;
    font-family: "Raleway", sans-serif; font-size: 19px; color: var(--muted); padding: 14px 15px; }
</style>
</head>
<body>
<div class="page">

  <nav class="site-nav">
    <a class="nav-link" style="left:103px" href="#about">About us</a>
    <a class="nav-link" style="left:288px" href="#services">Services</a>
    <div class="brand"><span class="brand-mark"></span><span class="brand-name">VALMIKE GROUP</span></div>
    <a class="nav-link" style="left:812px" href="#unit">Iron Finch</a>
    <a class="nav-link" style="left:1005px" href="#contact">Contact us</a>
  </nav>

  <header class="hero" role="img" aria-label="Aerial view of San Francisco skyline at sunset">
    <div class="hero-glow"></div>
    <h1 class="hero-title">NEW ERA IN PROTECTION.</h1>
    <p class="hero-sub">Providing the best executive protection since 1989</p>
    <a class="btn-solid" style="left:454px;top:250px;width:251px;height:58px" href="#contact">Get a Quote</a>
  </header>

  <section id="about">
    <p class="eyebrow" style="left:101px;top:965px">WHO WE ARE</p>
    <h2 class="heading" style="left:101px;top:1018px">LEADERS IN PRIVATE<br>SECURITY</h2>
    <p class="body-copy" style="left:101px;top:1180px;width:470px">Lorem ipsum dolor sit amet, consectetur adipiscing elit, sed do eiusmod tempor incididunt ut labore et dolore magna aliqua. Fermentum posuere urna nec tincidunt. Feugiat sed lectus vestibulum mattis ullamcorper velit sed ullamcorper.</p>
    <a class="btn-outline" style="left:101px;top:1494px;width:250px;height:58px" href="#about">Read More</a>
    <div class="photo" style="left:666px;top:939px;width:534px;height:766px;border-radius:4px 0 0 4px;background:linear-gradient(160deg,#e6eef2 0%,#c3dbe6 45%,#5b7584 75%,#2f3e48 100%)" role="img" aria-label="Security camera mounted before a glass skyscraper"></div>
  </section>

  <section id="services">
    <p class="eyebrow" style="left:101px;top:1774px">OUR SERVICES</p>
    <h2 class="heading" style="left:101px;top:1826px">WHAT WE OFFER</h2>

    <article class="service-card" style="left:101px;background:linear-gradient(90deg,#ecebe8 0%,#e2dfda 55%,#8a5a3e 72%,#2b3550 100%)" role="img" aria-label="Businessman walking with a leather briefcase">
      <span class="card-title">Executive Protection</span>
      <a class="card-link" href="#services">Learn More.</a>
    </article>
    <article class="service-card" style="left:581px;background:linear-gradient(90deg,#f4f4f4 0%,#e8e8e8 40%,#1b1b1b 70%,#111 100%)" role="img" aria-label="Potted plant beside a laptop on a white desk">
      <span class="card-title">Intelligence</span>
      <a class="card-link" href="#services">Learn More.</a>
    </article>
    <article class="service-card" style="left:1058px;background:linear-gradient(180deg,#a9cfe0 0%,#c9d9dc 60%,#b49a7c 100%)" role="img" aria-label="Chain-link fence against the sky">
      <span class="card-title">Covert Protection</span>
      <a class="card-link" href="#services">Learn More.</a>
    </article>
  </section>

  <section id="unit">
    <p class="eyebrow" style="left:101px;top:2545px">IRON FINCH</p>
    <h2 class="heading" style="left:101px;top:2593px">OUR SECURITY UNIT</h2>

    <h3 class="subhead" style="left:98px;top:2694px">TRAINING</h3>
    <p class="body-copy" style="left:98px;top:2751px;width:500px">Lorem ipsum dolor sit amet, consectetur adipiscing elit, sed do eiusmod tempor incididunt ut labore et dolore magna aliqua.</p>
    <a class="btn-outline" style="left:98px;top:2915px;width:249px;height:56px" href="#unit">Join Us</a>

    <h3 class="subhead" style="left:98px;top:3022px">CONSULTING</h3>
    <p class="body-copy" style="left:98px;top:3078px;width:500px">Lorem ipsum dolor sit amet, consectetur adipiscing elit, sed do eiusmod tempor incididunt ut labore et dolore magna aliqua.</p>
    <a class="btn-outline" style="left:98px;top:3241px;width:249px;height:57px" href="#unit">Our Team</a>

    <div class="photo" style="left:661px;top:2683px;width:539px;height:676px;border-radius:4px 0 0 4px;background:linear-gradient(170deg,#5d6a86 0%,#3c4663 45%,#2a3148 75%,#4a4350 100%)" role="img" aria-label="Downtown skyscrapers seen from above at dusk"></div>
  </section>

  <section id="contact">
    <p class="eyebrow" style="left:105px;top:3449px">CONTACT</p>
    <h2 class="heading" style="left:101px;top:3494px">GET TO KNOW US</h2>

    <div class="field" style="left:101px;top:3592px;width:427px;height:58px">Tell us your name</div>
    <div class="field" style="left:671px;top:3592px;width:426px;height:58px">Email Address</div>
    <div class="field" style="left:101px;top:3695px;width:427px;height:58px">Phone Number</div>
    <div class="field" style="left:671px;top:3695px;width:426px;height:58px">What's your business?</div>
    <div class="field" style="left:101px;top:3800px;width:996px;height:149px">Tell us how we can help you</div>

    <a class="btn-outline" style="left:101px;top:3996px;width:250px;height:56px" href="#contact">Submit</a>
  </section>

</div>
</body>
</html>
```